WordPress Design for both website and landing page for an expert

I need a clean and stylish design for my new website. I work as an expert (see attached file WHY HOW WHAT), my product is expert opinion (reports) for company evaluations You can use all of the attached pictures colored or black / white. The person is me, you can add other pictures, if you want. The design should be clean and stylish, so you could use white, black, gray, silver and / or one additional color. I have added an idea about my website, see attached file CONCEPT WEBSITE If you have any more information, please do not hesitate to contact us 'Hesitate to ask me ...

```html
<!DOCTYPE html>
<html lang="en">
<head>
<meta charset="utf-8">
<title>Lukas Brenner – Company Valuation Reports</title>
<link rel="stylesheet" href="https://fonts.googleapis.com/css2?family=Poppins:wght@300;400;500;600;700&display=swap">
<style>
:root{
  --ink:#0a0a0c;
  --ink-soft:#222;
  --sky:#22bdf5;
  --sky-deep:#0b7bb8;
  --mist:#d6dee2;
  --white:#ffffff;
  --grey:#7a7a7a;
  --field:#e6e6e6;
  --faint:#eef0f2;
  --hero-dark:#050608;
  --hero-mid:#18222c;
}
*{box-sizing:border-box;margin:0;padding:0}
html,body{width:1200px;height:2514px;overflow:hidden}
body{font-family:'Poppins',sans-serif;color:var(--ink-soft);background:var(--white);position:relative}

/* hero */
.hero{position:absolute;left:0;top:0;width:1200px;height:513px;background:var(--ink);overflow:hidden}
.hero-photo{position:absolute;left:478px;top:0;width:722px;height:513px;
  background:linear-gradient(100deg,var(--hero-dark) 0%,var(--hero-mid) 100%)}
.brand{position:absolute;left:66px;top:68px;font-size:16px;font-weight:400;letter-spacing:4px;color:var(--white);text-transform:uppercase}
.menu{position:absolute;left:1050px;top:30px;width:32px}
.menu span{display:block;height:2px;background:#bbb;margin-bottom:9px}
.hero-site{position:absolute;left:190px;top:216px;font-size:29px;font-weight:600;color:var(--sky)}
.hero-line{position:absolute;left:191px;top:275px;font-size:31px;font-weight:300;line-height:48px;color:#f2f2f2;width:560px}

/* welcome */
.welcome{position:absolute;left:0;top:513px;width:1200px;height:380px;background:var(--mist)}
.welcome h1{position:absolute;top:57px;width:100%;text-align:center;font-size:30px;font-weight:400;letter-spacing:4px;color:var(--ink)}
.welcome p{position:absolute;top:122px;left:200px;width:800px;text-align:center;font-size:17px;line-height:29px;color:#333}
.btn{position:absolute;top:236px;width:126px;height:41px;font-size:11.5px;font-weight:500;display:flex;align-items:center;justify-content:center}
.btn-primary{left:458px;background:var(--sky);color:var(--white)}
.btn-light{left:605px;background:var(--white);color:var(--ink)}
.wedge{position:absolute;left:0;width:1200px}

/* reasons */
.reasons-title{position:absolute;top:920px;width:100%;text-align:center;font-size:32px;font-weight:600;color:var(--ink-soft)}
.reasons-sub{position:absolute;top:968px;width:100%;text-align:center;font-size:17px;color:var(--ink-soft)}
.reason{position:absolute;top:1040px;width:300px;height:160px}
.reason-num{position:absolute;left:0;top:20px;font-size:150px;font-weight:700;line-height:150px;color:var(--faint)}
.reason-icon{position:absolute;top:0}
.reason h3{position:absolute;top:44px;font-size:27px;font-weight:400;color:var(--sky)}
.reason p{position:absolute;top:84px;width:170px;font-size:11px;line-height:16.5px;color:var(--grey)}

/* faq */
.faq-title{position:absolute;top:1350px;width:100%;text-align:center;font-size:31px;font-weight:600;color:#1d2a33}
.faq-sub{position:absolute;top:1393px;width:100%;text-align:center;font-size:16.5px;color:#0d3552}
.faq-list{position:absolute;left:150px;top:1462px;list-style:none}
.faq-list li{height:48.5px;font-size:15.5px;color:var(--white);display:flex;align-items:flex-start;padding-top:2px}
.faq-mark{width:14px;height:14px;border:2px solid var(--white);margin:4px 64px 0 6px;flex-shrink:0}
.note{position:absolute;left:150px;top:1772px;width:830px;font-size:15.5px;line-height:29px;color:var(--white)}
.note strong{font-weight:700;font-size:18px}

/* mailing */
.mailing{position:absolute;left:178px;top:1973px;width:844px;height:120px;background:var(--white);box-shadow:0 2px 14px rgba(0,0,0,.14)}
.mailing h2{position:absolute;left:35px;top:42px;font-size:23px;font-weight:400;color:#333}
.mailing .field{position:absolute;left:291px;top:36px;width:351px;height:51px;background:var(--field);font-size:11.5px;color:#777;padding:17px 22px}
.mailing .submit{position:absolute;left:657px;top:36px;width:148px;height:51px;background:var(--sky);color:var(--white);font-size:15px;font-weight:500;display:flex;align-items:center;justify-content:center}

/* footer */
.footer{position:absolute;left:0;top:2160px;width:1200px;height:354px;background:var(--ink)}
.foot-col{position:absolute;top:2282px}
.foot-col h4{font-size:19px;font-weight:600;color:var(--white);margin-bottom:14px}
.foot-about p{width:280px;font-size:12px;line-height:20.5px;color:var(--white)}
.contact-row{display:flex;align-items:center;font-size:12px;color:var(--white);height:24px}
.contact-row svg{margin-right:16px}
.social{display:flex;gap:16px;margin-top:2px}
.social span{width:16px;height:16px;border-radius:50%;background:var(--sky)}
.foot-rule{position:absolute;left:178px;top:2443px;width:844px;height:1px;background:#2a2a2a}
.copyright{position:absolute;top:2467px;width:100%;text-align:center;font-size:12px;color:var(--white)}
</style>
</head>
<body>

<header class="hero">
  <div class="hero-photo" role="img" aria-label="Portrait photograph of the valuation expert in a white shirt, leaning on a table"></div>
  <div class="brand">Lukas Brenner</div>
  <div class="menu"><span></span><span></span><span></span></div>
  <div class="hero-site">LUKASBRENNER.DE</div>
  <div class="hero-line">You need an opinion to determine the value of your company</div>
</header>

<section class="welcome">
  <h1>WELCOME!</h1>
  <p>Contrary to popular belief, Lorem Ipsum is not simply random text. It has roots in a piece of classical Latin literature from 45 BC, making it over 2000 years old.</p>
  <a class="btn btn-primary">About me</a>
  <a class="btn btn-light">Learn more</a>
</section>

<svg class="wedge" style="top:820px" width="1200" height="80" viewBox="0 0 1200 80">
  <polygon points="0,70 300,12 380,18 750,48 1050,6 1110,22 1200,44 1200,80 0,80" fill="var(--sky)"/>
  <polygon points="0,80 0,76 380,20 750,50 1110,22 1200,48 1200,80" fill="var(--white)"/>
</svg>

<div class="reasons-title">3 Reasons,</div>
<div class="reasons-sub">why you should work with me</div>

<div class="reason" style="left:165px">
  <div class="reason-num">1</div>
  <svg class="reason-icon" style="left:36px" width="42" height="34" viewBox="0 0 42 34" fill="none" stroke="#8a8a8a" stroke-width="1.6"><circle cx="26" cy="17" r="13"/><path d="M26 10v8l5 3M2 12h8M4 17h6M2 22h8"/></svg>
  <h3 style="left:40px">Fast</h3>
  <p style="left:41px">You will receive your report promptly (within a maximum of 21 days after receipt of all required documents)</p>
</div>
<div class="reason" style="left:480px">
  <div class="reason-num">2</div>
  <svg class="reason-icon" style="left:42px" width="38" height="32" viewBox="0 0 38 32" fill="none" stroke="#8a8a8a" stroke-width="1.6"><rect x="1" y="1" width="36" height="26"/><path d="M6 8h26M6 13h14M6 18h12"/><circle cx="28" cy="19" r="4"/><path d="M26 23v7l2-2 2 2v-7"/></svg>
  <h3 style="left:41px">Certified</h3>
  <p style="left:42px">You receive a qualified and reliable report from a certified expert (highest acceptance by all parties)</p>
</div>
<div class="reason" style="left:770px">
  <div class="reason-num">3</div>
  <svg class="reason-icon" style="left:26px;top:-4px" width="42" height="40" viewBox="0 0 42 40" fill="none" stroke="#8a8a8a" stroke-width="1.6"><circle cx="21" cy="20" r="9"/><path d="M17 29h8v6h-8zM21 2v5M6 8l4 4M36 8l-4 4M1 20h5M36 20h5"/></svg>
  <h3 style="left:39px">Understandable</h3>
  <p style="left:40px;width:200px">Your report will be logical and comprehensible for you and will not contain any "technical Chinese"</p>
</div>

<svg class="wedge" style="top:1262px" width="1200" height="660" viewBox="0 0 1200 660">
  <polygon points="0,0 590,30 1200,10 1200,600 0,600" fill="var(--sky)"/>
  <polygon points="0,418 1000,560 0,645" fill="var(--sky-deep)"/>
  <polygon points="0,645 1000,560 1200,610 1200,660 0,660" fill="var(--white)"/>
</svg>

<div class="faq-title">FAQ</div>
<div class="faq-sub">Frequently Asked Questions</div>
<ul class="faq-list">
  <li><span class="faq-mark"></span>What are the buying motives of the customers?</li>
  <li><span class="faq-mark"></span>You want to sell shares of your company or your entire company?</li>
  <li><span class="faq-mark"></span>You want to transfer your business to your heirs and need a valuation for the tax office?</li>
  <li><span class="faq-mark"></span>You have to pay someone in the context of a separation / divorce and need a tax base?</li>
  <li><span class="faq-mark"></span>Have your company evaluated by a qualified expert and avoid many (unnecessary) quarrels.</li>
</ul>
<p class="note"><strong>Note:</strong> The cost of a report are always disproportionately cheaper than the cost of legal disputes. And that detached from the psychological burden of such an argument ...</p>

<section class="mailing">
  <h2>Join my mailing list</h2>
  <div class="field">Enter your email id</div>
  <div class="submit">Submit</div>
</section>

<footer class="footer"></footer>
<svg class="wedge" style="top:2150px" width="1200" height="90" viewBox="0 0 1200 90">
  <polygon points="0,0 1200,0 1200,10 0,10" fill="var(--white)"/>
  <polygon points="0,10 300,68 740,28 1050,75 1200,45 1200,10" fill="var(--sky)"/>
  <polygon points="0,8 0,0 1200,0 1200,35 1120,55 740,22 300,58" fill="var(--white)"/>
</svg>

<div class="foot-col foot-about" style="left:178px">
  <h4>About</h4>
  <p>Contrary to popular belief, Lorem Ipsum is not simply random text. It has roots in a piece of classical Latin literature from 45 BC, making it over 2000 years old.</p>
</div>
<div class="foot-col" style="left:551px">
  <h4>Contact Us</h4>
  <div class="contact-row"><svg width="14" height="16" viewBox="0 0 14 16" fill="none" stroke="#666" stroke-width="1.2"><path d="M7 15s5-5 5-9A5 5 0 0 0 2 6c0 4 5 9 5 9z"/><circle cx="7" cy="6" r="2"/></svg>212 Harbor Lane, Millbrook, PA 15010</div>
  <div class="contact-row"><svg width="14" height="14" viewBox="0 0 14 14" fill="none" stroke="#666" stroke-width="1.2"><path d="M2 1l3 0 1 3-2 1a8 8 0 0 0 4 4l1-2 3 1v3c-6 0-10-4-10-10z"/></svg>800.555.0147</div>
  <div class="contact-row"><svg width="14" height="12" viewBox="0 0 14 12" fill="none" stroke="#666" stroke-width="1.2"><rect x="1" y="1" width="12" height="10"/><path d="M1 1l6 5 6-5"/></svg>contact@lukasbrenner.de</div>
</div>
<div class="foot-col" style="left:872px">
  <h4>Follow us</h4>
  <div class="social" aria-label="Social media links"><span></span><span></span><span></span><span></span><span></span></div>
</div>
<div class="foot-rule"></div>
<div class="copyright">© 2018 lukasbrenner.de.&nbsp; Careers &nbsp;-&nbsp; Privacy &nbsp;-&nbsp; Contact</div>

</body>
</html>
```